We need a full website with logo/graphics/woocommerce for hemp-based company

This site will be lunavetta.com. It is a website featuring the fact we are the only manufacturer to produce CBDP and THCP. It should be great on mobile and desktop. We will pay for any extensions needed and while it should be a simple site:

About Us
About the Laboratory
About CBDP
About THCP
Shop
Contact Us

Only 4 products on the site.

It can be wordpress or joomla. Your choice. You must install the final website on our server. We agree to pay for monthly support that must be submitted in your quote.

He have a great graphics designer that will assist keeping colors and graphics clean according to your specifications.

Industry/Entity Type

Hemp CBD THC

Coding

Coded - Design and coding required

Number of Pages Required

5+ page

Requirements
Must have
• A simple clean layout

```html
<!DOCTYPE html>
<html lang="en">
<head>
<meta charset="utf-8">
<title>Lunavetta – Laboratory Services</title>
<link href="https://fonts.googleapis.com/css2?family=Poppins:wght@400;500;600;700;800&display=swap" rel="stylesheet">
<style>
:root{
  --blue:#0a56ad;
  --blue-dark:#063f86;
  --green:#5a9a17;
  --green-light:#6bb01e;
  --ink:#1b1b1b;
  --muted:#7b7b7b;
  --night:#141a22;
  --white:#ffffff;
  --line:#d7dde6;
}
*{box-sizing:border-box;margin:0;padding:0}
html,body{width:1200px;height:3014px;overflow:hidden}
body{position:relative;background:var(--white);font-family:'Poppins',sans-serif;color:var(--ink)}
.abs{position:absolute}
.layer{position:absolute;left:0;top:0;width:1200px;height:3014px;pointer-events:none}

/* header */
.brand{left:88px;top:18px;display:flex;align-items:center;gap:8px}
.brand-dot{width:34px;height:34px;border-radius:50%;background:var(--blue)}
.brand-name{font-weight:700;font-size:25px;color:var(--blue);line-height:1}
.brand-tag{font-size:11px;color:var(--ink);margin-top:3px}
.nav{left:520px;top:31px;display:flex;gap:34px;font-size:13px;font-weight:500}
.nav a{color:var(--ink);text-decoration:none}
.nav a.active{color:var(--blue);font-weight:600;border-bottom:2px solid var(--blue);padding-bottom:2px}
.btn{display:inline-flex;align-items:center;justify-content:center;border-radius:22px;color:var(--white);font-weight:600;font-size:15px}
.btn-inquire{left:967px;top:21px;width:145px;height:35px;background:linear-gradient(90deg,var(--green),var(--blue-dark))}

/* hero */
.hero-title{left:88px;top:240px;font-size:48px;font-weight:800;color:var(--white);line-height:54px}
.btn-green{background:linear-gradient(90deg,var(--green),var(--green-light))}
.btn-blue{background:linear-gradient(90deg,var(--blue-dark),var(--blue))}
.hero-cta{left:91px;top:373px;width:158px;height:39px}
.flask-art{left:700px;top:310px;width:410px;height:290px;border-radius:40%;background:radial-gradient(circle at 45% 55%,rgba(110,200,60,.9),rgba(60,150,210,.75) 45%,rgba(40,130,200,0) 72%)}

/* about */
.section-title{font-size:36px;font-weight:700;color:var(--blue)}
.about-title{left:88px;top:714px}
.about-lead{left:88px;top:786px;width:470px;font-weight:600;font-size:16px;line-height:20px}
.about-text{left:88px;width:480px;font-size:15px;line-height:20px}
.about-more{left:88px;top:1030px;width:143px;height:39px}
.about-photo{left:706px;top:710px;width:406px;height:373px;border-radius:30px;background:linear-gradient(135deg,#8fb4d6,#3f77b5 50%,#253c5e)}
.about-badge{left:657px;top:879px;width:164px;height:164px;border-radius:22px;background:var(--white);box-shadow:0 8px 24px rgba(0,0,0,.15);display:flex;align-items:center;justify-content:center;gap:8px}
.about-badge span{font-weight:700;color:var(--blue);font-size:20px}
.badge-dot{width:18px;height:18px;border-radius:50%;background:var(--green)}

/* services */
.services-title{left:0;width:1200px;top:1318px;text-align:center;font-size:36px;font-weight:700;color:var(--white)}
.svc-card{width:437px;background:var(--white);border-radius:4px;overflow:hidden}
.svc-head{height:65px;background:var(--blue);display:flex;align-items:center;justify-content:space-between;padding:0 24px;color:var(--white);font-weight:700;font-size:28px}
.svc-head i{width:30px;height:30px;border-radius:50%;background:rgba(255,255,255,.35)}
.svc-body{padding:28px 24px 30px;font-size:14.5px;line-height:22px}
.svc-body .btn{width:146px;height:40px;margin-top:24px}
.svc-cbdp{left:147px;top:1453px}
.svc-thcp{left:616px;top:1404px}
.arrow{width:24px;height:24px}

/* team */
.team-title{left:0;width:1200px;top:1966px;text-align:center}
.member{top:2042px;width:212px;text-align:center}
.member-photo{height:202px;border-radius:14px;border:2px solid #e6e9ee;background:linear-gradient(180deg,#f4f6f9,#dde3ea)}
.member h3{color:var(--blue);font-size:15px;font-weight:600;margin-top:10px}
.member p{font-size:11.5px;color:var(--muted);line-height:14px;margin:6px 12px 0}
.socials{display:flex;gap:14px;justify-content:center;margin-top:14px}
.socials i{width:8px;height:8px;border-radius:50%;background:#444}

/* footer */
.inquiry-title{left:85px;width:480px;top:2482px;text-align:center;font-size:22px;font-weight:700;color:var(--blue)}
.field{left:190px;width:267px;height:37px;border:1px solid var(--line);border-radius:19px;font-size:12px;color:var(--muted);display:flex;align-items:center;gap:8px;padding:0 16px}
.field svg{width:12px;height:12px}
.field-msg{height:60px;align-items:flex-start;padding-top:11px;border-radius:14px}
.submit{left:262px;top:2782px;width:123px;height:37px}
.contact-head{font-size:16px;font-weight:600;color:var(--green-light)}
.c-item{display:flex;gap:12px;align-items:center}
.c-icon{width:42px;height:42px;border-radius:50%;background:var(--blue);display:flex;align-items:center;justify-content:center}
.c-icon svg{width:18px;height:18px}
.c-label{font-size:14px;color:#2f8ce0;line-height:17px}
.c-val{font-size:14px;color:var(--white);line-height:19px}
.hours{font-size:13px;line-height:20px;color:var(--white)}
.hours b{display:block;color:#2f8ce0;font-weight:500}
.foot-nav{left:88px;top:2945px;display:flex;gap:38px;font-size:14px;color:var(--white)}
.foot-nav span.active{color:var(--green-light);text-decoration:underline}
.copy{left:90px;top:2969px;font-size:12px;color:var(--white)}
.foot-social{left:1004px;top:2966px;display:flex;gap:22px}
.foot-social i{width:11px;height:11px;border-radius:50%;background:var(--white)}
</style>
</head>
<body>

<!-- decorative layer -->
<svg class="layer" viewBox="0 0 1200 3014" aria-hidden="true">
  <defs>
    <linearGradient id="photoTone" x1="0" y1="0" x2="1" y2="1">
      <stop offset="0" stop-color="#2b5f93"/><stop offset=".5" stop-color="#5d88b0"/><stop offset="1" stop-color="#24486f"/>
    </linearGradient>
    <linearGradient id="nightTone" x1="0" y1="0" x2="1" y2="1">
      <stop offset="0" stop-color="#252c36"/><stop offset="1" stop-color="#0f141b"/>
    </linearGradient>
  </defs>
  <!-- hero -->
  <path d="M0 77H1200V350C950 470 620 580 330 590C150 596 40 540 0 455Z" fill="url(#photoTone)" role="img" aria-label="Laboratory scientist working with a pipette"/>
  <path d="M0 462C40 555 150 610 330 608C620 600 880 520 1000 470" fill="none" stroke="#0a56ad" stroke-width="12"/>
  <path d="M600 568C820 510 1050 420 1200 345V375C1050 440 820 525 600 568Z" fill="#5a9a17"/>
  <!-- services -->
  <path d="M0 1365C330 1250 620 1180 880 1172C1040 1168 1150 1240 1200 1300V1700C1000 1800 620 1868 330 1872C150 1874 40 1810 0 1740Z" fill="url(#nightTone)" role="img" aria-label="Laboratory staff at work"/>
  <path d="M360 1210C560 1170 760 1162 880 1163C1040 1164 1160 1235 1200 1290" fill="none" stroke="#0a56ad" stroke-width="14"/>
  <path d="M0 1350C200 1280 400 1220 520 1198L520 1204C400 1232 200 1300 0 1370Z" fill="#5a9a17"/>
  <path d="M0 1745C40 1820 150 1885 330 1885C560 1882 800 1830 960 1780" fill="none" stroke="#0a56ad" stroke-width="12"/>
  <path d="M670 1862C880 1820 1070 1740 1200 1685V1715C1070 1770 880 1838 670 1862Z" fill="#5a9a17"/>
  <!-- footer -->
  <path d="M0 2710C330 2600 700 2520 950 2508C1080 2503 1170 2560 1200 2600V3014H0Z" fill="url(#nightTone)" role="img" aria-label="Laboratory scene in dark tones"/>
  <path d="M520 2550C700 2515 860 2500 950 2498C1080 2496 1170 2555 1200 2595" fill="none" stroke="#0a56ad" stroke-width="12"/>
  <path d="M0 2700C200 2640 420 2575 620 2535L620 2542C420 2590 200 2660 0 2735Z" fill="#5a9a17"/>
  <line x1="88" y1="2925" x2="1112" y2="2925" stroke="#2a313b" stroke-width="1"/>
  <!-- form hexagon -->
  <polygon points="200,2442 452,2442 560,2656 452,2870 200,2870 85,2656" fill="#fff" stroke="#0a56ad" stroke-width="4" stroke-linejoin="round"/>
  <polygon points="205,2452 447,2452 550,2656 447,2860 205,2860 96,2656" fill="none" stroke="#d7dde6" stroke-width="1" stroke-linejoin="round"/>
</svg>

<!-- header -->
<header>
  <div class="abs brand">
    <div class="brand-dot"></div>
    <div><div class="brand-name">Lunavetta</div><div class="brand-tag">The Only Purveyors Of CBDP &amp; THCP</div></div>
  </div>
  <nav class="abs nav">
    <a class="active" href="#">HOME</a><a href="#">ABOUT US</a><a href="#">TEAMS</a><a href="#">SHOP</a><a href="#">CONTACT US</a>
  </nav>
  <div class="abs btn btn-inquire">Inquire Now</div>
</header>

<!-- hero -->
<section>
  <h1 class="abs hero-title">Reliable &amp; High Quality<br>Laboratory Services</h1>
  <div class="abs btn btn-green hero-cta">Contact Us</div>
  <div class="abs flask-art" role="img" aria-label="Illustration of green and blue lab flasks with molecules"></div>
</section>

<!-- about -->
<section>
  <h2 class="abs section-title about-title">About Us</h2>
  <p class="abs about-lead">Lunavetta is the first lab to be able to make the minor cannabinoids TCHP and CBDP in bulk batches.</p>
  <p class="abs about-text" style="top:846px">These canniboids were are 2 of the 150 cannabinoids found in the hemp plant and 2 of the ones found in the smallest amounts.</p>
  <p class="abs about-text" style="top:906px;width:460px">Although most cannabis strains contain very small amounts of THCP and CBDP, the isolation of these phytocannabinoids have the potential to change the way we think about cannabinoids altogether.</p>
  <div class="abs btn btn-blue about-more">Read More</div>
  <div class="abs about-photo" role="img" aria-label="Lab technician in protective gear at a microscope"></div>
  <div class="abs about-badge"><i class="badge-dot"></i><span>Lunavetta</span></div>
</section>

<!-- services -->
<section>
  <h2 class="abs services-title">Services</h2>
  <article class="abs svc-card svc-cbdp">
    <div class="svc-head">CBDP<i></i></div>
    <div class="svc-body">Lorem Ipsum is simply dummy text of the printing and typesetting industry. Lorem Ipsum has been the industry's standard dummy text ever...<br><span class="btn btn-blue">Read More</span></div>
  </article>
  <article class="abs svc-card svc-thcp">
    <div class="svc-head">THCP<i></i></div>
    <div class="svc-body">Lorem Ipsum is simply dummy text of the printing and typesetting industry. Lorem Ipsum has been the industry's standard dummy text ever...<br><span class="btn btn-green">Read More</span></div>
  </article>
  <svg class="abs arrow" style="left:105px;top:1598px" viewBox="0 0 24 24"><circle cx="12" cy="12" r="10" fill="none" stroke="#aaa" stroke-width="2"/><path d="M17 12H8M11 8l-4 4 4 4" fill="none" stroke="#aaa" stroke-width="2"/></svg>
  <svg class="abs arrow" style="left:1071px;top:1524px" viewBox="0 0 24 24"><circle cx="12" cy="12" r="11" fill="#5a9a17"/><path d="M7 12h9M13 8l4 4-4 4" fill="none" stroke="#fff" stroke-width="2"/></svg>
</section>

<!-- team -->
<section>
  <h2 class="abs section-title team-title">Our Teams</h2>
  <svg class="abs arrow" style="left:104px;top:2135px" viewBox="0 0 24 24"><circle cx="12" cy="12" r="10" fill="none" stroke="#aaa" stroke-width="2"/><path d="M17 12H8M11 8l-4 4 4 4" fill="none" stroke="#aaa" stroke-width="2"/></svg>
  <svg class="abs arrow" style="left:1074px;top:2135px" viewBox="0 0 24 24"><circle cx="12" cy="12" r="10" fill="none" stroke="#5a9a17" stroke-width="2"/><path d="M7 12h9M13 8l4 4-4 4" fill="none" stroke="#5a9a17" stroke-width="2"/></svg>
  <div class="abs member" style="left:143px"><div class="member-photo" role="img" aria-label="Portrait of team member"></div><h3>Marcus Hale</h3><p>Lorem Ipsum is simply dummy text of the printing and typesetting industry.</p><div class="socials"><i></i><i></i><i></i><i></i></div></div>
  <div class="abs member" style="left:377px"><div class="member-photo" role="img" aria-label="Portrait of team member"></div><h3>Elena Varga</h3><p>Lorem Ipsum is simply dummy text of the printing and typesetting industry.</p><div class="socials"><i></i><i></i><i></i><i></i></div></div>
  <div class="abs member" style="left:611px"><div class="member-photo" role="img" aria-label="Portrait of team member"></div><h3>Owen Pritch</h3><p>Lorem Ipsum is simply dummy text of the printing and typesetting industry.</p><div class="socials"><i></i><i></i><i></i><i></i></div></div>
  <div class="abs member" style="left:846px"><div class="member-photo" role="img" aria-label="Portrait of team member"></div><h3>Nadia Kerr</h3><p>Lorem Ipsum is simply dummy text of the printing and typesetting industry.</p><div class="socials"><i></i><i></i><i></i><i></i></div></div>
</section>

<!-- footer -->
<footer>
  <h2 class="abs inquiry-title">Quick Inquiry</h2>
  <div class="abs field" style="top:2540px"><svg viewBox="0 0 12 12"><circle cx="6" cy="4" r="2.5" fill="none" stroke="#888"/><path d="M1.5 11.5c0-3 9-3 9 0" fill="none" stroke="#888"/></svg>Name</div>
  <div class="abs field" style="top:2589px"><svg viewBox="0 0 12 12"><rect x="3" y="1" width="6" height="10" rx="1" fill="none" stroke="#888"/></svg>Phone</div>
  <div class="abs field" style="top:2639px"><svg viewBox="0 0 12 12"><rect x="1" y="2.5" width="10" height="7" fill="none" stroke="#888"/><path d="M1 3l5 4 5-4" fill="none" stroke="#888"/></svg>Email</div>
  <div class="abs field field-msg" style="top:2689px"><svg viewBox="0 0 12 12"><rect x="1.5" y="1.5" width="9" height="9" fill="none" stroke="#888"/></svg>Message</div>
  <div class="abs btn btn-green submit">Submit</div>

  <div class="abs contact-head" style="left:638px;top:2597px">Conatct Info</div>
  <div class="abs c-item" style="left:638px;top:2619px"><div class="c-icon"><svg viewBox="0 0 18 18"><path d="M9 17s-6-6-6-10a6 6 0 0112 0c0 4-6 10-6 10z" fill="#fff"/><circle cx="9" cy="7" r="2" fill="#0a56ad"/></svg></div><div class="c-val">14 Orchard Row, Fenwick,<br>Ashby,LE6 2QT</div></div>
  <div class="abs c-item" style="left:904px;top:2619px"><div class="c-icon"><svg viewBox="0 0 18 18"><path d="M4 2l3 3-2 2c1 2 3 4 5 5l2-2 3 3-2 3C7 16 2 11 1 4z" fill="#fff"/></svg></div><div><div class="c-label">Phone</div><div class="c-val">07000 123456</div></div></div>
  <div class="abs c-item" style="left:638px;top:2684px"><div class="c-icon"><svg viewBox="0 0 18 18"><rect x="2" y="4" width="14" height="10" rx="1" fill="#fff"/><path d="M2 5l7 5 7-5" fill="none" stroke="#0a56ad" stroke-width="1.5"/></svg></div><div><div class="c-label">Email</div><div class="c-val" style="font-size:15px">info@lunavetta.com</div></div></div>
  <div class="abs c-item" style="left:904px;top:2684px"><div class="c-icon"><svg viewBox="0 0 18 18"><rect x="5" y="2" width="8" height="5" fill="#fff"/><rect x="2" y="7" width="14" height="7" rx="1" fill="#fff"/><rect x="5" y="11" width="8" height="5" fill="#fff" stroke="#0a56ad"/></svg></div><div><div class="c-label">Telephone/Fax</div><div class="c-val" style="font-size:15px">01000 654321</div></div></div>

  <div class="abs contact-head" style="left:638px;top:2776px">Open Hours</div>
  <div class="abs hours" style="left:638px;top:2813px"><b>Mon - Fri</b>Open 24 Hours</div>
  <div class="abs hours" style="left:801px;top:2813px"><b>Saturday</b>6:00 - 18:00</div>
  <div class="abs hours" style="left:945px;top:2813px"><b>Sunday</b>Appointment Only</div>

  <div class="abs foot-nav"><span class="active">Home</span><span>About us</span><span>Teams</span><span>Shop</span><span>Contact Us</span></div>
  <div class="abs copy">Copyright © Lunavetta. All Rights Reserved</div>
  <div class="abs foot-social"><i></i><i></i><i></i><i></i></div>
</footer>

</body>
</html>
```